2020 Lone Ridge Crisis Alliance Conference Event flyer for annual conference held in Amarillo Texas

The Power of Connection

I need a flyer to send out via email. I The flyer will depict our theme, "The Power of Connection" event dates, website and costs. Association is Lone Ridge Crisis Alliance, date April 23-25, 2020, website www.loneridgealliance.org, Early Bird and Member discounts location Harborview Lodge, Amarillo Texas

page 2 will have sponsor info, and keynote description, can be 3 pages if absolutely necessary
: keynote speaker Martin Oakley, Martin is a retired Westbrook Roadway Patrol officer who spent more than 17 years patrolling the Silverfall Span Bridge. During that time he encountered hundreds of people who were troubled and had lost hope. They were ready to jump off the bridge and end their lives. Although a trained negotiator, Oakley also relied on his compassion, gentle voice, eye contact, and his innate ability to “listening to understand”. During his career, he encouraged more than 200 people not to jump, go over the bridge’s rail or come back to solid ground from where they had been standing precariously. These challenging, but rewarding efforts earned him the nickname, “Guardian of the Silverfall Span Bridge”. Retired, Oakley is now dedicating his life to promoting mental health awareness and suicide prevention across the globe.
Great sponsor opportunities available at www.Loneridgealliance.org sponsor letter attached for info on sponsor opportunities it is not necessary to include all info

i attached a mockup page 1 flyer that i really like but graphic designer did not complete this would give you an idea of what i am looking for on page 1 although it is missing a few elements

the Brookhaven (logo attached) is a champion sponsor, Plainsview Visitors Bureau (logo attached)

Target Market(s)

law enforcement, hospitals, mental health providers, court system,

Colors

Designer to choose colors to be used in the design.

Requirements
Must have
• theme -The Power of Connection
• website
• dates
• location
• costs
Nice to have
• prefer graphic related to theme
• Brookhaven is a large sponsor
• need to have 2-3 pages for all info
• include info on sponsor opportunities but does not have to include all info on attachment

```html
<!DOCTYPE html>
<html lang="en">
<head>
<meta charset="utf-8">
<title>2020 Lone Ridge Crisis Alliance Conference</title>
<link href="https://fonts.googleapis.com/css2?family=Bebas+Neue&family=Cinzel:wght@500;600&family=Poppins:wght@500;600;700&display=swap" rel="stylesheet">
<style>
  :root {
    --backdrop: #47484a;
    --paper: #ffffff;
    --navy: #22409a;
    --red: #e0262b;
    --deep-red: #8c1a1c;
    --stripe-red: #d5323a;
    --stripe-plum: #9b3560;
    --forest: #1f5a35;
    --forest-light: #2f7a48;
    --gold: #d59a3e;
    --ink: #3a3a3c;
    --white: #ffffff;
  }
  * { margin: 0; padding: 0; box-sizing: border-box; }
  html, body { width: 976px; height: 1200px; overflow: hidden; background: var(--backdrop); }
  .flyer {
    position: absolute; left: 66px; top: 56px; width: 844px; height: 1088px;
    background: var(--paper); overflow: hidden;
  }
  .hero { position: absolute; left: 0; top: 0; width: 844px; height: 462px; }
  .hero-art { position: absolute; left: 0; top: 0; }
  .theme {
    position: absolute; left: 548px; top: 66px; width: 286px;
    font-family: "Bebas Neue", "Oswald", sans-serif; color: var(--gold);
    font-size: 100px; line-height: 84px; text-align: center; letter-spacing: 1px;
  }
  .theme-last { display: block; font-size: 70px; line-height: 78px; letter-spacing: 0; }
  .brand {
    position: absolute; left: 38px; top: 494px; width: 206px; text-align: center;
  }
  .brand-mark {
    width: 150px; height: 150px; margin: 0 auto 10px; border-radius: 50%;
    border: 9px solid var(--navy);
  }
  .brand-name {
    font-family: "Cinzel", "Times New Roman", serif; font-weight: 600;
    color: var(--navy); font-size: 17px; line-height: 21px;
  }
  .title {
    position: absolute; left: 286px; top: 508px; width: 550px; text-align: center;
    font-family: "Cinzel", "Times New Roman", serif; font-weight: 600;
  }
  .title-main { display: block; color: var(--navy); font-size: 44px; line-height: 52px; }
  .title-sub { display: block; color: var(--red); font-size: 54px; line-height: 64px; }
  .details { position: absolute; left: 38px; top: 718px; width: 770px; height: 192px; }
  .details-bands { position: absolute; left: 0; top: 0; }
  .when-where {
    position: absolute; left: 0; top: 0; width: 384px; height: 192px;
    color: var(--white); text-align: center;
  }
  .label {
    display: flex; align-items: center; justify-content: center; gap: 12px;
    font-family: "Bebas Neue", "Oswald", sans-serif; font-size: 42px; line-height: 42px;
  }
  .label .icon {
    width: 36px; height: 36px; border-radius: 50%; border: 2px solid var(--gold);
    display: flex; align-items: center; justify-content: center; flex: none;
  }
  .when .label { margin-top: 12px; }
  .value-date {
    font-family: "Cinzel", "Times New Roman", serif; font-weight: 500;
    font-size: 30px; line-height: 40px;
  }
  .where .label { margin-top: 8px; }
  .value-place {
    font-family: "Cinzel", "Times New Roman", serif; font-weight: 500;
    font-size: 17px; line-height: 30px; letter-spacing: 0.3px;
  }
  .offer {
    position: absolute; left: 420px; top: 0; width: 350px; height: 192px;
    display: flex; align-items: center; justify-content: center; text-align: center;
    font-family: "Poppins", sans-serif; font-weight: 700; color: var(--white);
    font-size: 36px; line-height: 48px;
  }
  .website {
    position: absolute; left: 0; top: 926px; width: 844px;
    display: flex; align-items: center; justify-content: center; gap: 12px;
    font-family: "Poppins", sans-serif; font-weight: 600; color: var(--ink); font-size: 21px;
  }
  .divider { position: absolute; left: 82px; top: 977px; width: 678px; height: 2px; background: var(--red); }
  .sponsors {
    position: absolute; left: 0; top: 994px; width: 844px; height: 60px;
    display: flex; align-items: center; justify-content: center; gap: 34px;
  }
  .sponsor-bureau {
    font-family: "Cinzel", "Times New Roman", serif; font-weight: 600;
    color: var(--gold); font-size: 21px; line-height: 24px; text-align: center;
  }
  .sponsor-health { display: flex; align-items: center; gap: 10px; }
  .sponsor-health .square { width: 44px; height: 44px; background: var(--forest); }
  .sponsor-health .name { font-family: "Poppins", sans-serif; font-weight: 700; font-size: 24px; line-height: 28px; color: #111; }
  .sponsor-health .sub { font-family: "Poppins", sans-serif; font-weight: 500; font-size: 13px; color: #111; }
</style>
</head>
<body>
<main class="flyer">
  <section class="hero">
    <svg class="hero-art" width="844" height="462" viewBox="0 0 844 462">
      <defs>
        <linearGradient id="hall" x1="0" y1="0" x2="0.3" y2="1">
          <stop offset="0" stop-color="#a4482a"/>
          <stop offset="0.45" stop-color="#8c5a4c"/>
          <stop offset="1" stop-color="#6a6e7a"/>
        </linearGradient>
        <radialGradient id="burst" cx="0.55" cy="0.5" r="0.7">
          <stop offset="0" stop-color="#2f7a48"/>
          <stop offset="1" stop-color="#1f5a35"/>
        </radialGradient>
      </defs>
      <rect width="844" height="462" fill="url(#hall)" role="img" aria-label="Speaker presenting to a seated conference audience"/>
      <polygon points="598,0 844,0 844,462 590,462 466,228" fill="url(#burst)"/>
      <polyline points="598,0 466,228 590,462" fill="none" stroke="#ffffff" stroke-width="5"/>
    </svg>
    <h2 class="theme">THE<br>POWER<br>OF<span class="theme-last">CONNECTION</span></h2>
  </section>

  <div class="brand">
    <div class="brand-mark"></div>
    <div class="brand-name">Lone Ridge<br>Crisis Alliance</div>
  </div>

  <h1 class="title">
    <span class="title-main">2020 LONE RIDGE<br>CRISIS ALLIANCE</span>
    <span class="title-sub">CONFERENCE</span>
  </h1>

  <section class="details">
    <svg class="details-bands" width="770" height="192" viewBox="0 0 770 192">
      <polygon points="400,0 770,0 770,192 400,192 440,96" fill="#8c1a1c"/>
      <polygon points="384,0 408,0 448,96 408,192 384,192 424,96" fill="#d5323a"/>
      <polygon points="370,0 388,0 428,96 388,192 370,192 410,96" fill="#9b3560"/>
      <polygon points="0,0 376,0 416,96 376,192 0,192" fill="#22409a"/>
      <polyline points="412,10 762,10 762,182 412,182 448,96 412,10" fill="none" stroke="#ffffff" stroke-width="2" stroke-dasharray="8 5"/>
    </svg>
    <div class="when-where">
      <div class="when">
        <div class="label"><span class="icon">
          <svg width="18" height="18" viewBox="0 0 18 18"><rect x="1" y="3" width="16" height="14" rx="2" fill="none" stroke="#d59a3e" stroke-width="2"/><line x1="1" y1="7" x2="17" y2="7" stroke="#d59a3e" stroke-width="2"/><line x1="5" y1="1" x2="5" y2="5" stroke="#d59a3e" stroke-width="2"/><line x1="13" y1="1" x2="13" y2="5" stroke="#d59a3e" stroke-width="2"/></svg>
        </span>DATE</div>
        <div class="value-date">APRIL 23-25, 2020</div>
      </div>
      <div class="where">
        <div class="label"><span class="icon">
          <svg width="16" height="20" viewBox="0 0 16 20"><path d="M8 1a7 7 0 0 0-7 7c0 5 7 11 7 11s7-6 7-11a7 7 0 0 0-7-7z" fill="#d59a3e"/><circle cx="8" cy="8" r="2.6" fill="#22409a"/></svg>
        </span>LOCATION</div>
        <div class="value-place">HARBORVIEW LODGE, AMARILLO TEXAS</div>
      </div>
    </div>
    <div class="offer">Early Bird<br>and Member<br>Discounts</div>
  </section>

  <div class="website">
    <svg width="26" height="26" viewBox="0 0 26 26"><circle cx="13" cy="13" r="12" fill="#3a3a3c"/><g fill="none" stroke="#ffffff" stroke-width="1.4"><ellipse cx="13" cy="13" rx="5" ry="12"/><line x1="1" y1="13" x2="25" y2="13"/><line x1="3" y1="7" x2="23" y2="7"/><line x1="3" y1="19" x2="23" y2="19"/></g></svg>
    <span>www.loneridgealliance.org</span>
  </div>

  <div class="divider"></div>

  <footer class="sponsors">
    <div class="sponsor-bureau">PLAINSVIEW<br>VISITORS BUREAU</div>
    <div class="sponsor-health">
      <div class="square"></div>
      <div>
        <div class="name">The Brookhaven</div>
        <div class="sub">High Plains Regional Health</div>
      </div>
    </div>
  </footer>
</main>
</body>
</html>
```